Book Postcard Design

We need a postcard design to promote the book written by our founder and president, Lior Beckett. The book is titled KESTRL: The Craft and Logic of Momentum. We're open to any eye-catching image designs you come up with.

```html
<!DOCTYPE html>
<html lang="en">
<head>
<meta charset="utf-8">
<title>KESTRL Book Postcard</title>
<link href="https://fonts.googleapis.com/css2?family=Arimo:wght@400;700&family=Questrial&display=swap" rel="stylesheet">
<style>
  :root{
    --bg:#c4c4c4;
    --blue:#2196d8;
    --blue-light:#4cb4ea;
    --blue-deep:#1678bd;
    --grey:#6b6b6b;
    --white:#ffffff;
    --ink:#222222;
    --stamp:#c8c8c8;
  }
  *{margin:0;padding:0;box-sizing:border-box}
  html,body{width:1200px;height:1200px;overflow:hidden;background:var(--bg)}
  body{position:relative;font-family:"Arimo",Arial,sans-serif;color:var(--white)}

  .card{position:absolute;overflow:hidden}
  .front{left:70px;top:47px;width:712px;height:551px;background:var(--grey)}
  .front__blue{position:absolute;left:0;top:0;width:712px;height:423px;
    background:radial-gradient(circle at 30% 20%,var(--blue-light),var(--blue) 55%,var(--blue-deep))}
  .front__panel{position:absolute;left:0;top:0}
  .book{position:absolute;border-radius:3px;
    background:linear-gradient(100deg,#d9d9d9 0%,#f7f7f7 12%,#ffffff 50%,#ececec 100%)}
  .front .book{left:474px;top:49px;width:208px;height:324px}
  .front__title{position:absolute;left:20px;top:26px;width:440px;text-align:center;
    font-family:"Questrial",sans-serif;font-weight:700;line-height:1.2}
  .front__title h1{font-size:38px;font-weight:700;-webkit-text-stroke:.6px var(--white)}
  .front__title h2{font-size:32px;font-weight:700;-webkit-text-stroke:.5px var(--white);margin-top:2px}
  .front__rule{position:absolute;left:100px;top:117px;width:250px;height:1px;background:rgba(255,255,255,.6)}
  .front__body{position:absolute;left:22px;top:132px;width:410px;font-size:14px;line-height:17.5px}
  .front__body p{margin-bottom:7px}
  .front__body .lead{font-weight:700;font-size:17.5px;line-height:21px;margin-top:8px}
  .front__proof{position:absolute;left:19px;top:427px;width:670px;font-size:15px;line-height:19.5px}
  .front__proof strong{font-size:23px}
  .front__call{position:absolute;left:0;top:503px;width:712px;display:flex;align-items:center;gap:10px;font-size:20px}
  .front__call .line{flex:1;height:2px;background:var(--white)}
  .phone{display:inline-block;vertical-align:-3px}

  .back{left:479px;top:634px;width:670px;height:518px;background:var(--white)}
  .back__side{position:absolute;left:0;top:0;width:323px;height:518px;
    background:radial-gradient(circle at 60% 40%,var(--blue-light),var(--blue) 55%,var(--blue-deep))}
  .back__head{position:absolute;left:0;top:0;width:323px;height:73px;background:var(--grey);
    padding:20px 0 0 20px;font-size:17px;line-height:22px}
  .back .book{left:61px;top:98px;width:180px;height:240px}
  .back__note{position:absolute;left:23px;top:357px;font-size:15px;line-height:23px}
  .back__sign{position:absolute;left:23px;top:409px;font-size:19px;font-weight:700}
  .back__tab{position:absolute;left:0;top:442px}
  .back__call{position:absolute;left:0;top:450px;width:323px;text-align:center;color:var(--blue);font-weight:700;font-size:20px;line-height:24px}
  .back__call .num{letter-spacing:2px}
  .stamp{position:absolute;left:594px;top:25px;width:42px;height:53px;background:var(--stamp)}
  .address-line{position:absolute;left:451px;width:183px;height:1.5px;background:var(--ink)}
</style>
</head>
<body>

<section class="card front">
  <div class="front__blue"></div>
  <svg class="front__panel" width="712" height="423" viewBox="0 0 712 423">
    <polygon points="464,0 712,0 712,397 420,397" fill="#ffffff"/>
  </svg>
  <div class="book" role="img" aria-label="Hardcover book mockup: KESTRL, The Craft and Logic of Momentum, by Lior Beckett"></div>

  <div class="front__title">
    <h1>Read the Book “KESTRL”</h1>
    <h2>For better Results</h2>
  </div>
  <div class="front__rule"></div>

  <div class="front__body">
    <p>We know how difficult training can be in your industry. Unlike children, whose sponge-like minds are ripe for training, you work with adults. Adults have unique opinions and established habits that can make them unruly trainees.</p>
    <p>That’s why we’re here. The Beckett Group is a consulting and training organization, and we’ve worked with hundreds of businesses across a dozen industries (including business to business and business to consumer enterprises) to help refine their training and make their business more effective. Businesses experience an average growth of 20% within the first year of working with The Beckett Group.</p>
    <p class="lead">We’re the experts on adult behavior change; we know the ins-and-outs of the hows and whys, and we can help you gain that knowledge, too.</p>
  </div>

  <p class="front__proof"><strong>Need proof?</strong> That’s why we’ve sent along this copy of KESTRL: The Craft and Logic of Momentum. In this book I break down the six step process I’ve refined to enact adult behavioral change. It’s a quick and easy read, and I think you’ll enjoy it.</p>

  <div class="front__call">
    <span class="line"></span>
    <span>To give us a call Please dial
      <svg class="phone" width="22" height="22" viewBox="0 0 22 22"><circle cx="11" cy="11" r="9.5" fill="none" stroke="#fff" stroke-width="1.6"/><path d="M7.3 6.2l2 .1.9 2.6-1.2 1c.7 1.4 1.7 2.4 3.1 3.1l1-1.2 2.6.9.1 2c-.3.6-1 .9-1.7.9-4.1-.4-7.3-3.6-7.7-7.7 0-.7.3-1.4.9-1.7z" fill="#fff"/></svg>15550142876</span>
    <span class="line"></span>
  </div>
</section>

<section class="card back">
  <div class="back__side"></div>
  <div class="back__head">Once you’ve read <strong>KESTRL</strong>, you might be inspired to change your business</div>
  <div class="book" role="img" aria-label="Hardcover book mockup: KESTRL, The Craft and Logic of Momentum, by Lior Beckett"></div>
  <p class="back__note">When that happens, give us a call.<br>We’d love to help.</p>
  <p class="back__sign">Lior Beckett, Founder &amp; CEO</p>
  <svg class="back__tab" width="323" height="76" viewBox="0 0 323 76">
    <polygon points="29,0 293,0 321,76 5,76" fill="#ffffff"/>
  </svg>
  <div class="back__call">
    To give us a call dial<br>
    <svg class="phone" width="22" height="22" viewBox="0 0 22 22"><circle cx="11" cy="11" r="9.5" fill="none" stroke="#333" stroke-width="1.6"/><path d="M7.3 6.2l2 .1.9 2.6-1.2 1c.7 1.4 1.7 2.4 3.1 3.1l1-1.2 2.6.9.1 2c-.3.6-1 .9-1.7.9-4.1-.4-7.3-3.6-7.7-7.7 0-.7.3-1.4.9-1.7z" fill="#333"/></svg><span class="num">15550142876</span>
  </div>

  <div class="stamp"></div>
  <div class="address-line" style="top:210px"></div>
  <div class="address-line" style="top:248px"></div>
  <div class="address-line" style="top:291px"></div>
</section>

</body>
</html>
```